CRESTLINE Academy Exhibit Booth Posters

My company is CRESTLINE Academy (a division of CRESTLINE for Growth). We are exhibiting in a month, and I need to re-do my exhibit booth posters. There will be a total of 4 posters needed. Sizes are below.
1) Top- 11 feet long X 12 inches wide (Try to match color scheme in example photo)
2) Center- 4 feet long X 2 feet wide (Chalkboard background)
3) Left- 18 inches long X 2 feet wide (Cork-board back ground with the use of push pins holding up post-it-notes, paper, etc.)
4) Right- 18 inches long X 2 feet wide (Cork-board back ground with the use of push pins holding up post-it-notes, paper, etc.)
I have attached a photo of my old booth. This will get you an idea of the size, color schemes, and more. I have created basic rendering of each poster. The content is important, but the look and design should be drastically improved.
The websites to look into for ideas are:
www.crestlineforgrowth.example
www.crestlineacademy.example
Updates
I've added a new file. It's a .JPG of the certification diploma. Thanks!
Target Market(s)
Business Owners, Managers, HR, Supervisors, Teens who want to boost their resume
Industry/Entity Type
It Company
Look and feel

```html
<!DOCTYPE html>
<html lang="en">
<head>
<meta charset="utf-8">
<title>CRESTLINE Academy – Booth Header Banner</title>
<link rel="stylesheet" href="https://fonts.googleapis.com/css2?family=Cinzel:wght@700&family=Libre+Baskerville:wght@700&display=swap">
<style>
  :root {
    --blush: #f7e6ec;
    --rose: #e88c9e;
    --crimson: #cf2f3f;
    --deep-red: #b3202f;
    --navy: #1b2058;
    --midnight: #121640;
    --sky: #bfe1f2;
    --white: #ffffff;
    --title-red: #b5121b;
    --tagline-magenta: #c0158a;
    --brand-navy: #1f3a8a;
  }
  html, body {
    margin: 0;
    padding: 0;
    overflow: hidden;
    background: var(--white);
  }
  .banner {
    position: relative;
    width: 1200px;
    height: 100px;
    overflow: hidden;
  }
  .banner-backdrop {
    position: absolute;
    inset: 0;
    display: block;
  }
  .brand {
    position: absolute;
    left: 14px;
    top: 22px;
    display: flex;
    align-items: center;
    gap: 8px;
  }
  .brand-dot {
    width: 18px;
    height: 18px;
    border-radius: 50%;
    background: var(--brand-navy);
    flex: none;
  }
  .brand-name {
    font-family: "Libre Baskerville", Georgia, serif;
    font-weight: 700;
    font-size: 15px;
    line-height: 1.25;
    color: var(--brand-navy);
    margin: 0;
  }
  .banner-title {
    position: absolute;
    left: 0;
    right: 0;
    top: 4px;
    margin: 0 0 0 150px;
    text-align: center;
    font-family: "Cinzel", "Times New Roman", serif;
    font-weight: 700;
    font-size: 50px;
    line-height: 56px;
    letter-spacing: 3px;
    color: var(--title-red);
    -webkit-text-stroke: 1.5px var(--white);
    paint-order: stroke fill;
    text-shadow: 2px 3px 3px rgba(60, 0, 10, 0.55);
  }
  .banner-tagline {
    position: absolute;
    left: 0;
    right: 0;
    top: 60px;
    margin: 0 0 0 135px;
    text-align: center;
    font-family: "Libre Baskerville", Georgia, serif;
    font-weight: 700;
    font-size: 20px;
    line-height: 26px;
    color: var(--tagline-magenta);
    -webkit-text-stroke: 3px var(--white);
    paint-order: stroke fill;
    text-shadow: 1px 2px 2px rgba(40, 0, 40, 0.35);
  }
</style>
</head>
<body>
<header class="banner">
  <svg class="banner-backdrop" width="1200" height="100" viewBox="0 0 1200 100" aria-hidden="true">
    <defs>
      <linearGradient id="sweep" x1="0" y1="0" x2="1" y2="0">
        <stop offset="0" stop-color="var(--blush)"/>
        <stop offset="0.14" stop-color="var(--rose)"/>
        <stop offset="0.32" stop-color="var(--crimson)"/>
        <stop offset="0.6" stop-color="var(--crimson)"/>
        <stop offset="0.75" stop-color="var(--deep-red)"/>
        <stop offset="0.88" stop-color="#4a2f63"/>
        <stop offset="1" stop-color="var(--navy)"/>
      </linearGradient>
      <linearGradient id="glow" x1="0" y1="0" x2="0" y2="1">
        <stop offset="0" stop-color="#ffffff" stop-opacity="0.35"/>
        <stop offset="0.5" stop-color="#ffffff" stop-opacity="0"/>
      </linearGradient>
      <linearGradient id="sky-wave" x1="0" y1="0" x2="1" y2="0">
        <stop offset="0" stop-color="var(--sky)"/>
        <stop offset="0.6" stop-color="#e6f3fa"/>
        <stop offset="1" stop-color="#9fb4d6"/>
      </linearGradient>
    </defs>
    <rect class="backdrop-base" width="1200" height="100" fill="url(#sweep)"/>
    <rect class="backdrop-glow" width="1200" height="100" fill="url(#glow)"/>
    <path class="wave-highlight" d="M820 100 C900 60 1000 30 1200 18 L1200 28 C1010 40 920 70 860 100 Z" fill="#ffffff" opacity="0.25"/>
    <path class="wave-highlight" d="M900 100 C980 70 1080 50 1200 44 L1200 50 C1090 58 1000 78 940 100 Z" fill="#ffffff" opacity="0.2"/>
    <path class="wave-navy" d="M700 100 C850 86 1000 70 1200 58 L1200 100 Z" fill="var(--midnight)" opacity="0.85"/>
    <path class="wave-sky" d="M0 78 C200 96 450 98 700 92 C900 86 1050 80 1200 78 L1200 86 C1050 90 900 96 720 100 L0 100 Z" fill="url(#sky-wave)"/>
    <path class="wave-edge" d="M0 76 C200 94 450 96 700 90 C900 84 1050 78 1200 76" fill="none" stroke="#ffffff" stroke-width="2" opacity="0.9"/>
  </svg>

  <div class="brand">
    <span class="brand-dot"></span>
    <p class="brand-name">CRESTLINE<br>Academy</p>
  </div>

  <h1 class="banner-title">CRESTLINE ACADEMY</h1>
  <p class="banner-tagline">Training School for a Workforce with Limited Work Experience</p>
</header>
</body>
</html>
```